Sign Advertisment for Condominium Development

I need a sign created that will be placed in front of a building that is being converted into a luxury condominium development.

The sign needs to say:

Two, Boutique Luxury Condominiums Delivering late 2015.

Luxury Finishes // Designer Kitchens and Bath // Each Unit over 2,000 Square Feet

Deeded Parking Included with Each Unit

To Learn More, Contact:

Loretta Pinwell or Morgan Tesh
(202) 555-0147
Loretta.Pinwell@nrg-example.com

I need a small disclaimer at the bottom stating:

These Condominium(s) have not been registered by the Office of Residential Property Oversight Bureau of Dwelling Registration Tenancy Transfer and Purchase Section. A Condominium Unit may be reserved on a non-binding reservation agreement, but no contract of sale or lease that is binding on the purchaser may be entered into prior to registration.

Target Market(s)

Young professionals seeking luxury condominium

Industry/Entity Type

Building

Font styles to use
Serif

Colors
00a88f
ffffff

```html
<!DOCTYPE html>
<html lang="en">
<head>
<meta charset="utf-8">
<title>Two Boutique Luxury Condominiums – Sign</title>
<link rel="stylesheet" href="https://fonts.googleapis.com/css2?family=Open+Sans:ital,wght@0,300;0,400;1,300&display=swap">
<style>
  :root {
    --navy: #262640;
    --white: #ffffff;
    --paper: #ffffff;
    --ink: #3a3a3a;
    --ink-soft: #555555;
    --fine-print: #6b6b96;
    --rule: rgba(255, 255, 255, 0.35);
    --room-light: #f1efec;
    --room-mid: #d9d4cf;
    --room-floor: #8a7f79;
  }
  * { margin: 0; padding: 0; box-sizing: border-box; }
  html, body {
    width: 1200px; height: 800px; overflow: hidden;
    background: var(--paper);
    font-family: "Open Sans", Arial, sans-serif;
  }
  .sign { position: relative; width: 1200px; height: 800px; overflow: hidden; background: var(--paper); }

  .interior-photo {
    position: absolute; left: 400px; top: 0; width: 800px; height: 577px;
    background: linear-gradient(180deg, var(--room-light) 0%, #e8e4e0 45%, var(--room-mid) 62%, var(--room-floor) 100%);
  }

  .navy-panel { position: absolute; left: 0; top: 0; width: 1200px; height: 800px; }

  .brand {
    position: absolute; left: 75px; top: 78px; width: 255px;
    color: var(--white); font-weight: 400; text-align: center;
    display: flex; flex-direction: column; align-items: center; gap: 6px;
  }
  .brand-mark { width: 14px; height: 14px; background: var(--white); margin-bottom: 6px; }
  .brand-name { font-size: 31px; letter-spacing: 1px; line-height: 1; }
  .brand-sub { font-size: 16px; letter-spacing: 1.5px; line-height: 1; }

  .headline {
    position: absolute; left: 40px; top: 288px; width: 420px;
    color: var(--white); text-align: center;
    font-style: italic; font-weight: 300; font-size: 29px;
    letter-spacing: 2.5px; line-height: 42px; text-transform: uppercase;
  }

  .features {
    position: absolute; left: 95px; top: 482px; width: 310px;
    list-style: none; color: var(--white); text-align: center;
    font-weight: 300; font-size: 16px;
  }
  .features li { line-height: 33px; border-bottom: 1px solid var(--rule); }
  .features li:last-child { border-bottom: none; }

  .disclaimer {
    position: absolute; right: 28px; top: 586px; width: 690px;
    color: var(--fine-print); font-size: 10px; line-height: 15px; text-align: right;
  }

  .contact { position: absolute; right: 17px; top: 736px; text-align: right; }
  .contact-title { font-size: 19px; color: var(--ink); line-height: 26px; }
  .contact-line { font-size: 13.5px; color: var(--ink-soft); line-height: 22px; word-spacing: 1px; }
  .contact-line .sep { margin: 0 18px; }
</style>
</head>
<body>
<main class="sign">
  <div class="interior-photo" role="img" aria-label="Photograph of a bright furnished condominium living room with open kitchen, bar stools, sofas and carpet"></div>

  <svg class="navy-panel" viewBox="0 0 1200 800" aria-hidden="true">
    <polygon points="0,0 400,0 600,345 400,800 0,800" fill="var(--navy)"/>
  </svg>

  <div class="brand">
    <span class="brand-mark"></span>
    <span class="brand-name">NORTHRIDGE</span>
    <span class="brand-sub">RESIDENTIAL GROUP, LLC</span>
  </div>

  <h1 class="headline">Two<br>Boutique Luxury<br>Condominiums<br>Delivering Late 2015.</h1>

  <ul class="features">
    <li>Luxury Finishes</li>
    <li>Designer Kitchens and Bath</li>
    <li>Each Unit over 2,000 Square Feet</li>
    <li>Deeded Parking Included with Each Unit</li>
  </ul>

  <p class="disclaimer">These Condominium(s) have not been registered by the Office of Residential Property Oversight Bureau of Dwelling Registration Tenancy Transfer and Purchase Section. A Condominium Unit may be reserved on a non-binding reservation agreement, but no contract of sale or lease that is binding on the purchaser may be entered into prior to registration.</p>

  <div class="contact">
    <p class="contact-title">To Learn More, Contact:</p>
    <p class="contact-line">Loretta Pinwell or Morgan Tesh<span class="sep">|</span>(202) 555-0147<span class="sep">|</span>Loretta.Pinwell@nrg-example.com</p>
  </div>
</main>
</body>
</html>
```